Seriöses Webdesign für innovatives Ingenieurbüro mit dem Schwerpunkt Eisenbahn Leit- und Sicherungstechnik
Zielgruppe
Die Webseite hat in erster Linie die Aufgabe zu informieren: An erster Stelle steht die Kontaktaufnahme und der Kompetenzbereich des Ingenieurbüros.
Folgende Kernkompetenzen sollen durch die Webseite transportiert werden:
Hardware-Entwicklung
Software-Entwicklung
Erneuerung alter Techniken
Begutachtung
Software für Lieferantenbewertung
Störungsmanagement(system)
Zielgruppe:
Die Webseite soll als Online-Visitenkarte für bestehende und neue Kontakte dienen. Gerade neue (Messe-)Kontakte erleben die Webseite als erste Anlaufstelle und erhalten einen Einblick in das vorhandene Leistungsspektrum des Ingenieurbüros und die Möglichkeiten der Kontaktaufnahme.

```html
<!DOCTYPE html>
<html lang="de">
<head>
<meta charset="utf-8">
<title>Vekta Consult – Ingenieurbüro</title>
<link href="https://fonts.googleapis.com/css2?family=Source+Sans+3:wght@400;600;700&display=swap" rel="stylesheet">
<style>
:root{
  --sky:#7bc3e2;
  --ink:#2c3841;
  --ink-soft:#3a4751;
  --accent:#6ab8dc;
  --paper:#ffffff;
  --grey:#e6e6e6;
  --text:#2b2f33;
}
*{margin:0;padding:0;box-sizing:border-box}
html,body{width:922px;height:1200px;overflow:hidden}
body{font-family:"Source Sans 3",sans-serif;color:var(--text);background:var(--paper);position:relative}
.abs{position:absolute}
.header{left:0;top:0;width:922px;height:76px;background:var(--sky)}
.brand{left:138px;top:18px;font-size:28px;font-weight:700;color:#fff;letter-spacing:.2px}
.lang{left:732px;top:28px;width:60px;height:22px;background:#a8d8ec;display:flex;align-items:center;gap:4px;padding-left:2px;font-size:8.5px;font-weight:700}
.lang span{padding:2px 5px}
.lang .on{background:#fff;color:var(--ink)}
.lang .off{color:var(--ink)}
.nav{left:140px;top:76px;height:34px;display:flex;border-left:1px solid #a9b4bc;border-right:1px solid #a9b4bc}
.nav a{display:flex;align-items:center;padding:0 6px;font-size:12px;font-weight:600;color:var(--ink);text-decoration:none;border-right:1px solid #c6ced3}
.nav a:last-child{border-right:none}
.nav a.active{background:var(--ink);color:#fff}
.hero{left:0;top:110px;width:922px;height:237px;background:linear-gradient(180deg,#7d8fa6 0%,#9aa6b4 45%,#c9cdd2 62%,#8a8a7a 78%,#a3a08a 100%)}
.intro{left:0;top:350px;width:922px;height:240px;background:var(--ink)}
.intro h1{left:137px;top:28px;font-size:32px;line-height:35px;font-weight:400;color:#fff}
.intro .art{left:307px;top:20px;width:219px;height:72px;background:var(--ink-soft)}
.intro .sub{left:137px;top:102px;font-size:15px;font-weight:600;color:var(--accent)}
.intro p{left:137px;top:151px;width:305px;font-size:11px;line-height:17px;color:#fff}
.contact{left:597px;top:86px;color:#fff}
.contact h2{font-size:24px;font-weight:700;color:var(--accent);line-height:28px}
.contact .phone{font-size:10.5px;font-weight:700;margin-top:4px}
.contact .day{font-size:10.5px;font-weight:700;color:var(--accent);margin-top:10px;line-height:12px}
.contact .hours{font-size:8.5px;font-weight:600;line-height:12px}
.contact .day + .hours + .day{margin-top:3px}
.col{top:624px;width:186px}
.col .head{display:flex;align-items:flex-end;gap:14px;height:40px}
.col h3{font-size:16px;font-weight:600;letter-spacing:.4px;color:var(--ink);line-height:18px}
.col p{font-size:11px;line-height:15.5px;margin-top:15px}
.col p.lead{color:var(--accent)}
.col p + p{margin-top:15px}
.detail{left:0;top:874px;width:922px;height:225px;background:var(--grey)}
.parts{left:167px;top:51px;width:149px;height:136px;background:linear-gradient(90deg,#b9b2a4 0%,#c9c3b7 40%,#e6e6e6 50%,#6f8f6c 62%,#55704f 100%)}
.detail h2{left:382px;top:62px;font-size:25px;line-height:29px;font-weight:700;color:var(--ink)}
.detail p{font-size:10.5px;line-height:15.5px;color:var(--text);width:200px}
.footer{left:0;top:1101px;width:922px;height:99px;background:var(--sky)}
.footbrand{left:136px;top:31px;font-size:18px;font-weight:700;color:#fff}
.btn{left:600px;top:37px;width:127px;height:23px;border:1px solid #fff;color:#fff;font-size:10.5px;font-weight:700;display:flex;align-items:center;justify-content:center}
.links{left:136px;top:71px;font-size:9.5px;font-weight:600;color:var(--ink)}
</style>
</head>
<body>
<header class="abs header">
  <div class="abs brand">Vekta Consult</div>
  <div class="abs lang"><span class="on">DE</span><span class="off">ENG</span></div>
</header>
<nav class="abs nav">
  <a href="#">Hardware</a><a href="#">Software</a><a href="#">Erneuerung</a><a href="#" class="active">Begutachtung</a><a href="#">Lieferantenbewertung</a><a href="#">Störungsmanagement</a>
</nav>
<div class="abs hero" role="img" aria-label="Foto: drei Hochgeschwindigkeitszüge fahren aus einer Halle auf Gleisen zu"></div>

<section class="abs intro">
  <h1 class="abs">Wir stellen<br>Weichen</h1>
  <div class="abs art" role="img" aria-label="Illustration: gepunkteter Weg von einem Monitor zu Weichengleisen"></div>
  <div class="abs sub">Maßgeschneiderte Softwarelösungen</div>
  <p class="abs">Hier sollte ein Text stehen, der uns zum Vorteil gereift. Hier sollte ein Text stehen, der uns zum Vorteil gereift. Hier sollte ein Text stehen, der uns zum Vorteil</p>
  <div class="abs contact">
    <h2>Kontakt zu uns</h2>
    <div class="phone">0 800 - 47 21 90 00</div>
    <div class="day">Montag – Donnerstag</div>
    <div class="hours">08:00 – 12:00 Uhr / 13:30 – 17:00 Uhr</div>
    <div class="day">Freitag</div>
    <div class="hours">8:00 – 12:00 Uhr</div>
  </div>
</section>

<section>
  <div class="abs col" style="left:138px">
    <div class="head">
      <svg width="34" height="32" viewBox="0 0 34 32"><rect x="6" y="1" width="27" height="16" fill="none" stroke="#2c3841" stroke-width="1.5"/><circle cx="7" cy="13" r="3" fill="#2c3841"/><circle cx="17" cy="13" r="3" fill="#2c3841"/><circle cx="28" cy="22" r="3" fill="#2c3841"/><rect x="1" y="17" width="12" height="8" rx="3" fill="#2c3841"/><rect x="12" y="17" width="11" height="8" rx="3" fill="#2c3841"/><rect x="23" y="26" width="11" height="6" rx="2" fill="#2c3841"/><rect x="3" y="26" width="8" height="6" fill="#2c3841"/><rect x="13" y="26" width="8" height="6" fill="#2c3841"/></svg>
      <h3>Schulungen</h3>
    </div>
    <p class="lead">Hier sollte ein Text stehen, der uns zum Vorteil gereift. Hier sollte ein Text stehen.</p>
    <p>Hier sollte ein Text stehen, der uns zum Vorteil gereift. Hier sollte ein Text stehen. Hier sollte ein Text stehen, der uns zum Vorteil gereift. Hier sollte ein Text stehen.</p>
  </div>
  <div class="abs col" style="left:382px">
    <div class="head">
      <svg width="26" height="40" viewBox="0 0 26 40"><circle cx="9" cy="3" r="2" fill="#2c3841"/><circle cx="17" cy="3" r="2" fill="#2c3841"/><rect x="1" y="6" width="24" height="28" rx="6" fill="#2c3841"/><rect x="5" y="11" width="16" height="8" rx="1" fill="#fff"/><circle cx="7" cy="27" r="2" fill="#fff"/><circle cx="19" cy="27" r="2" fill="#fff"/><path d="M5 34 L2 40 M21 34 L24 40" stroke="#2c3841" stroke-width="2"/></svg>
      <h3>Spezialgebiete</h3>
    </div>
    <p class="lead">Hier sollte ein Text stehen, der uns zum Vorteil gereift. Hier sollte ein Text stehen. Hier sollte ein Text stehen.Hier sollte ein Text stehen.</p>
    <p>Hier sollte ein Text stehen, der uns zum Vorteil gereift. Hier sollte ein</p>
  </div>
  <div class="abs col" style="left:602px">
    <div class="head">
      <svg width="22" height="20" viewBox="0 0 22 20"><rect x="8" y="0" width="6" height="8" fill="#2c3841"/><path d="M4 8 H18 L11 15 Z" fill="#2c3841"/><path d="M1 12 V19 H21 V12" fill="none" stroke="#2c3841" stroke-width="2.5"/></svg>
      <h3>Downloads</h3>
    </div>
    <p>Hier sollte ein Text stehen, der uns zum Vorteil gereift.</p>
  </div>
</section>

<section class="abs detail">
  <div class="abs parts" role="img" aria-label="Foto: zwei Relais-Bauteile mit durchsichtigem Gehäuse"></div>
  <h2 class="abs">In Kleinigkeiten<br>ganz groß</h2>
  <p class="abs" style="left:382px;top:128px">Hier sollte ein Text stehen, der uns zum Vorteil gereift. Hier sollte ein Text stehen, der uns zum Vorteil gereift.</p>
  <p class="abs" style="left:604px;top:67px">Hier sollte ein Text stehen, der uns zum Vorteil gereift. Hier sollte ein Text stehen, der uns zum Vorteil gereift.</p>
  <p class="abs" style="left:604px;top:129px">Hier sollte ein Text stehen, der uns zum Vorteil gereift. Hier sollte ein Text stehen, der uns zum Vorteil gereift.</p>
</section>

<footer class="abs footer">
  <div class="abs footbrand">Vekta</div>
  <div class="abs btn">Nachricht senden &gt;&gt;</div>
  <div class="abs links">Startseite &nbsp;•&nbsp; AGB &nbsp;•&nbsp; Bankverbindung &nbsp;•&nbsp; Datenschutz &nbsp;•&nbsp; Impressum</div>
</footer>
</body>
</html>
```